Ashcombe Heritage Guild Harvest Lantern Days Event Flyer - Historic Event

I need a flyer about the Ashcombe Heritage Guild's Harvest Lantern Days event October 8th and 9th. The centerpiece of Harvest Lantern Days is Civil War reenactments. I want the flyer to include the schedule of events and be eye catching on area bulletin boards. Our website is www.ashcombeheritageguild.org for more information and pictures. The website for the Calder Ridge Rangers reenactors is http://www.calderridgerangers.com/.

Target Market(s)

Our target market is middle ages (35-70) families and couples. Most are history buffs, especially about the Civil War.

Industry/Entity Type

Non-Profit

Font styles to use
Serif
Decorative
Script

Requirements
Must have
• The flyer must include the majority of the schedule attached - especially the battle times, museums, and anything including food.The dance on Saturday night is also important. The bottom of the flyer MUST say "Paid in part by Quillan County Visitor Levy Board"
Nice to have
• Pictures

```html
<!DOCTYPE html>
<html lang="en">
<head>
<meta charset="utf-8">
<title>Ashcombe Heritage Guild's Harvest Lantern Days</title>
<link rel="stylesheet" href="https://fonts.googleapis.com/css2?family=Open+Sans:wght@300;400;600;700&family=Quicksand:wght@300;400&display=swap">
<style>
  :root {
    --bg: #3a3226;
    --gold: #d8b56e;
    --gold-line: #b8955a;
    --cream: #f3e6c8;
    --orange: #e8742a;
    --sepia-dark: #7d6540;
    --sepia-light: #d2b57a;
  }
  * { margin: 0; padding: 0; box-sizing: border-box; }
  html, body { width: 849px; height: 1200px; overflow: hidden; background: var(--bg); }
  .flyer {
    position: relative; width: 849px; height: 1200px; overflow: hidden;
    background: var(--bg);
    font-family: "Open Sans", sans-serif;
  }
  .photo-band { position: absolute; inset: 0; }
  .event-dates {
    position: absolute; right: 53px; top: 30px;
    color: var(--orange); font-weight: 700; font-size: 48px; letter-spacing: 0.5px;
  }
  .event-dates sup { font-size: 26px; vertical-align: 18px; line-height: 0; }
  .contact { position: absolute; right: 48px; text-align: right; color: var(--cream); font-weight: 600; }
  .contact-host { top: 103px; font-size: 19px; }
  .contact-phone { top: 140px; font-size: 27px; }
  .contact-email { top: 187px; font-size: 15px; }
  .title {
    position: absolute; left: 40px; top: 218px; width: 420px; text-align: right;
    color: var(--gold); text-shadow: 0 2px 6px rgba(40,25,10,0.55); line-height: 1;
  }
  .title-host { display: block; font-weight: 300; font-size: 66px; text-align: left; letter-spacing: 1px; }
  .title-org { display: block; font-weight: 400; font-size: 35px; margin-top: 8px; }
  .title-event { display: block; font-weight: 700; font-size: 46px; margin-top: 10px; }
  .title-event-days { display: block; font-weight: 700; font-size: 60px; margin-top: 2px; }
  .schedule {
    position: absolute; left: 42px; top: 634px; width: 375px;
    font-family: "Quicksand", sans-serif; font-weight: 300;
    color: var(--cream); font-size: 14px; line-height: 18.6px;
  }
  .schedule-day { color: var(--orange); font-weight: 400; font-size: 17px; line-height: 22px; text-transform: uppercase; }
  .schedule-day + .schedule-list { margin-bottom: 2px; }
  .schedule-list { list-style: none; }
  .funding {
    position: absolute; left: 0; right: 0; top: 1100px; text-align: center;
    color: var(--orange); font-size: 27px; font-weight: 400;
  }
  .website {
    position: absolute; left: 0; right: 0; top: 1145px; text-align: center;
    color: var(--gold); font-size: 22px; font-weight: 400;
  }
</style>
</head>
<body>
<main class="flyer">
  <svg class="photo-band" width="849" height="1200" viewBox="0 0 849 1200">
    <defs>
      <linearGradient id="sepiaTone" x1="0" y1="0" x2="1" y2="1">
        <stop offset="0" stop-color="#6e5a3a"/>
        <stop offset="0.5" stop-color="#c9a96a"/>
        <stop offset="1" stop-color="#a8864e"/>
      </linearGradient>
      <linearGradient id="streetTone" x1="0" y1="0" x2="1" y2="1">
        <stop offset="0" stop-color="#8e6a3e"/>
        <stop offset="0.35" stop-color="#9c4a34"/>
        <stop offset="0.7" stop-color="#2a2e3e"/>
        <stop offset="1" stop-color="#5f6a3a"/>
      </linearGradient>
      <linearGradient id="carriageTone" x1="0" y1="0" x2="1" y2="1">
        <stop offset="0" stop-color="#c98a58"/>
        <stop offset="1" stop-color="#7a4a2e"/>
      </linearGradient>
    </defs>
    <polygon role="img" aria-label="Sepia photograph of two women in period dress under a parasol" points="0,0 200,0 560,220 0,330" fill="url(#sepiaTone)"/>
    <polygon role="img" aria-label="Photograph of a Victorian brick house, a vintage car and fiddlers in Civil War uniform" points="560,220 849,496 849,960 0,356 0,330" fill="url(#streetTone)" opacity="0.95"/>
    <line x1="200" y1="0" x2="849" y2="496" stroke="var(--gold-line)" stroke-width="5"/>
    <line x1="0" y1="356" x2="849" y2="960" stroke="var(--gold-line)" stroke-width="5"/>
    <rect role="img" aria-label="Photograph of antique horse-drawn buggies in a museum" x="437" y="869" width="220" height="162" rx="16" fill="url(#carriageTone)" stroke="var(--gold-line)" stroke-width="4"/>
  </svg>

  <div class="event-dates">OCTOBER 8<sup>th</sup>-9<sup>th</sup></div>
  <p class="contact contact-host">ASHCOMBE HERITAGE GUILD'S</p>
  <p class="contact contact-phone">(555)014-2873</p>
  <p class="contact contact-email">AshcombeHeritageGuild@mailbox.org</p>

  <h1 class="title">
    <span class="title-host">ASHCOMBE</span>
    <span class="title-org">HERITAGE GUILD'S</span>
    <span class="title-event">HARVEST LANTERN</span>
    <span class="title-event-days">DAYS</span>
  </h1>

  <section class="schedule">
    <h2 class="schedule-day">Saturday, October 8th, 2016</h2>
    <ul class="schedule-list">
      <li>Through the Day – Demonstrations and Speakers in various locations</li>
      <li>10:00 AM – Battle by Calder Ridge Rangers</li>
      <li>Sponsored in part by Marlowe's Corner Markets</li>
      <li>11:30-1:00 – Chicken Biscuit Bake at Town Hall – Free Will Donation</li>
      <li>Afternoon – Trolley and Buggy Rides</li>
      <li>1:00-4:00 Museums Opens</li>
      <li>1:30-2:00 Birthday Cake on Pemberton House Front Porch</li>
      <li>Cake donated by Kettleby Grocers - Harlan Falls</li>
      <li>2:00 Battle by Calder Ridge Rangers</li>
      <li>3:00-Sightseeing Cruise on the Ashcombe Belle</li>
      <li>6:00-? Dance at Town Hall with Turntable Band</li>
      <li>Sponsored by Dr. Ellery</li>
    </ul>
    <h2 class="schedule-day">Sunday, October 9th, 2016</h2>
    <ul class="schedule-list">
      <li>12:30 PM Parade on Main Street</li>
      <li>Afternoon – Buggy &amp; Trolley Rides</li>
      <li>1:00-4:00 Museums Open</li>
      <li>1:30 Battle by Calder Ridge Rangers</li>
      <li>2:00- Pie Reception at Ashcombe Depot and Railroad History Museum</li>
      <li>3:00-Sightseeing Cruise</li>
    </ul>
  </section>

  <p class="funding">Paid in part by Quillan County Visitor Levy Board</p>
  <p class="website">www.ashcombeheritageguild.org</p>
</main>
</body>
</html>
```